Larkspur Business Card Design

Looking for elegant and super stylish business cards. Enclosed is the card design we are using now. We need something more contemporary.

Target Market(s)

We are a catering company focusing on weddings and corporate events.

Industry/Entity Type

Caterer

Contact Information for Business Card

Please use similar font to our current cards

Colors
0592cd

Requirements
Must have
• Color and be very unique. Also, please use logo (with or without the castle.)

```html
<!DOCTYPE html>
<html lang="en">
<head>
<meta charset="utf-8">
<title>Larkspur Business Card</title>
<link href="https://fonts.googleapis.com/css2?family=Marcellus&family=Arimo:wght@400;700&display=swap" rel="stylesheet">
<style>
  :root {
    --backdrop: #2b2b2b;
    --card-white: #ffffff;
    --card-shade: #e4e4e4;
    --brand-blue: #0592cd;
    --brand-blue-deep: #0a6fa3;
    --ink: #111111;
    --ink-soft: #6a6a6a;
    --on-blue: #ffffff;
  }
  * { box-sizing: border-box; margin: 0; padding: 0; }
  html, body { width: 1200px; height: 997px; overflow: hidden; }
  body { background: var(--backdrop); font-family: "Arimo", Arial, sans-serif; position: relative; }

  .card {
    position: absolute;
    width: 540px; height: 310px;
    background: linear-gradient(160deg, var(--card-white) 55%, var(--card-shade));
    box-shadow: 0 18px 40px rgba(0,0,0,.55);
    overflow: hidden;
  }
  .card--front { left: 60px; top: 150px; }
  .card--back { left: 600px; top: 440px; }

  /* brand lockup */
  .brand { position: absolute; display: flex; align-items: center; gap: 18px; }
  .brand__mark { width: 104px; height: 104px; background: var(--ink); }
  .brand__text { font-family: "Marcellus", Georgia, serif; color: var(--ink); }
  .brand__name { font-size: 40px; letter-spacing: 2px; line-height: 1; }
  .brand__tagline { font-size: 14px; letter-spacing: 6px; line-height: 1.25; margin-top: 4px; color: var(--ink); }

  .card--front .brand { left: 46px; top: 58px; }

  .web-band {
    position: absolute; left: 0; top: 200px; width: 100%; height: 40px;
    background: var(--brand-blue);
    color: var(--on-blue);
    font-weight: 700; font-size: 15px; letter-spacing: 2.5px;
    display: flex; align-items: center; justify-content: center;
  }

  /* back */
  .back-field { position: absolute; inset: 0; }
  .card--back .brand { left: 200px; top: 34px; }
  .card--back .brand__name { font-size: 34px; }
  .card--back .brand__tagline { font-size: 12px; letter-spacing: 5px; }

  .person { position: absolute; left: 26px; top: 196px; }
  .person__name { font-weight: 700; font-size: 15px; color: var(--ink); letter-spacing: .5px; }
  .person__role { font-size: 13px; color: var(--on-blue); margin-top: 3px; }

  .contacts { position: absolute; left: 26px; top: 244px; list-style: none; }
  .contacts li { display: flex; align-items: center; gap: 8px; color: var(--on-blue); font-size: 13px; line-height: 18px; }
  .contacts svg { width: 13px; height: 13px; flex: none; }

  .address { position: absolute; right: 24px; top: 150px; text-align: right; color: var(--on-blue); font-size: 13px; line-height: 17px; }
</style>
</head>
<body>

  <section class="card card--front" aria-label="Card front">
    <div class="brand">
      <div class="brand__mark"></div>
      <div class="brand__text">
        <div class="brand__name">THE LARKSPUR</div>
        <div class="brand__tagline">CATERING &amp;<br>EVENT DESIGN</div>
      </div>
    </div>
    <div class="web-band">www.larkspurcatering.com</div>
  </section>

  <section class="card card--back" aria-label="Card back">
    <svg class="back-field" viewBox="0 0 540 310" preserveAspectRatio="none" aria-hidden="true">
      <defs>
        <linearGradient id="blueField" x1="0" y1="0" x2="0" y2="1">
          <stop offset="0" stop-color="#0592cd"/>
          <stop offset="1" stop-color="#0a6fa3"/>
        </linearGradient>
      </defs>
      <polygon points="0,190 540,92 540,310 0,310" fill="url(#blueField)"/>
    </svg>

    <div class="brand">
      <div class="brand__text">
        <div class="brand__name">THE LARKSPUR</div>
        <div class="brand__tagline">CATERING &amp;<br>EVENT DESIGN</div>
      </div>
    </div>

    <div class="person">
      <div class="person__name">MARCUS HALDEN</div>
      <div class="person__role">Chief Executive Officer</div>
    </div>

    <ul class="contacts">
      <li>
        <svg viewBox="0 0 14 14"><circle cx="7" cy="7" r="7" fill="#fff"/><rect x="3.5" y="5" width="7" height="5" rx="1" fill="#0a6fa3"/><rect x="5" y="3" width="4" height="2.5" fill="#0a6fa3"/></svg>
        555 210 4471 &nbsp; ext 302
      </li>
      <li>
        <svg viewBox="0 0 14 14"><circle cx="7" cy="7" r="7" fill="#fff"/><path d="M4 5.5c1-2 5-2 6 0l-1 1.2H8.2L7.8 6H6.2l-.4.7H5z" fill="#0a6fa3"/><rect x="4.5" y="7.5" width="5" height="3" rx=".8" fill="#0a6fa3"/></svg>
        555 380 1296
      </li>
      <li>
        <svg viewBox="0 0 14 14"><circle cx="7" cy="7" r="7" fill="#fff"/><rect x="3.5" y="4.5" width="7" height="5" fill="#0a6fa3"/><path d="M3.5 4.5 7 7.5l3.5-3" stroke="#fff" stroke-width=".8" fill="none"/></svg>
        m@larkspurcatering.com
      </li>
    </ul>

    <div class="address">4120 Marlow Avenue, Bayview<br>California 90000</div>
  </section>

</body>
</html>
```